I need a simple, classy and stylish business card. I would like it to have a black background with white writing. I would like you to use my logo you designed on the front with the word 'Imagery" used underneath it in the same font. On the back I was thinking of the website at the top 'tomvarley.com' Then my social media accounts, Can you use the instagram, Facebook and twitter logo then my handles?
Please let me know what you think.
Regards Tom
Industry/Entity Type
Business
Requirements
Must have
- Website: www.tomvarley.com
- Social media handles..
- Instagram: @Tom_Varley_Imagery
- Facebook: Tom Varley Imagery
- Twitter: @Tom_Varley
- Email: info@tomvarly.com
- Phone: 0437 581 904

```html
<!DOCTYPE html>
<html lang="en">
<head>
<meta charset="utf-8">
<title>Tom Varley Imagery – Business Card</title>
<link rel="stylesheet" href="https://fonts.googleapis.com/css2?family=Montserrat:wght@300;400;600&display=swap">
<style>
  :root {
    --backdrop: #8f8a84;
    --card-clear: #eceae7;
    --card-black: #0b0b0c;
    --ink-dark: #1d1d1f;
    --ink-muted: #5c5c60;
    --logo-tone: #d8d1c6;
    --card-radius: 22px;
  }
  * { margin: 0; padding: 0; box-sizing: border-box; }
  html, body {
    width: 1200px;
    height: 969px;
    overflow: hidden;
    background: var(--backdrop);
    font-family: "Montserrat", Arial, sans-serif;
  }
  .canvas {
    position: relative;
    width: 1200px;
    height: 969px;
  }
  .business-card {
    position: absolute;
    left: 100px;
    top: 198px;
    width: 1000px;
    height: 570px;
    border-radius: var(--card-radius);
    overflow: hidden;
    background: var(--card-clear);
    box-shadow: 0 18px 40px rgba(0,0,0,0.28);
  }
  .card-shapes {
    position: absolute;
    inset: 0;
    width: 100%;
    height: 100%;
  }
  .card-shapes .black-panel,
  .card-shapes .swoosh { fill: var(--card-black); }

  .holder {
    position: absolute;
    left: 42px;
    top: 58px;
  }
  .holder-name {
    font-weight: 600;
    font-size: 31px;
    letter-spacing: 0.5px;
    color: var(--ink-dark);
    line-height: 1.1;
  }
  .holder-title {
    font-weight: 400;
    font-size: 24px;
    letter-spacing: 0.5px;
    color: var(--ink-muted);
    margin-top: 4px;
  }

  .contact-list {
    position: absolute;
    left: 48px;
    top: 343px;
    list-style: none;
  }
  .contact-item {
    display: flex;
    align-items: center;
    height: 38px;
    font-size: 24px;
    font-weight: 400;
    letter-spacing: 0.6px;
    color: var(--ink-dark);
  }
  .contact-icon {
    width: 22px;
    height: 22px;
    margin-right: 16px;
    flex: none;
    fill: var(--ink-dark);
  }
  .contact-mark {
    width: 18px;
    height: 18px;
    margin: 0 18px 0 2px;
    flex: none;
    background: var(--ink-dark);
    border-radius: 3px;
  }
  .contact-mark.round { border-radius: 50%; }

  .brand {
    position: absolute;
    left: 710px;
    top: 92px;
    color: var(--logo-tone);
    font-weight: 300;
  }
  .brand-dot {
    position: absolute;
    left: -68px;
    top: 14px;
    width: 52px;
    height: 52px;
    border-radius: 50%;
    border: 3px solid var(--logo-tone);
  }
  .brand-name {
    font-size: 50px;
    line-height: 1;
    letter-spacing: 1px;
    white-space: nowrap;
  }
  .brand-sub {
    font-size: 36px;
    line-height: 1;
    margin: 10px 0 0 66px;
    letter-spacing: 1px;
  }
</style>
</head>
<body>
<main class="canvas">
  <section class="business-card">
    <svg class="card-shapes" viewBox="0 0 548 312" preserveAspectRatio="none" aria-hidden="true">
      <path class="swoosh" d="M212 38 C194 122 258 222 410 312 L398 312 C248 226 188 130 212 38 Z"/>
      <path class="black-panel" d="M222 0 C204 62 214 140 300 210 C360 258 428 290 468 312 L548 312 L548 0 Z"/>
    </svg>

    <div class="holder">
      <p class="holder-name">SAM ROWE</p>
      <p class="holder-title">PRESIDENT</p>
    </div>

    <ul class="contact-list">
      <li class="contact-item">
        <svg class="contact-icon" viewBox="0 0 24 24" aria-hidden="true">
          <path d="M3 8c0-2 3-4 9-4s9 2 9 4v2h-5V8c-1-.6-2.5-1-4-1s-3 .4-4 1v2H3z"/>
          <path d="M6 12h12l2 8H4z"/>
        </svg>
        0437 581 904
      </li>
      <li class="contact-item">
        <svg class="contact-icon" viewBox="0 0 24 24" aria-hidden="true">
          <circle cx="12" cy="12" r="10"/>
        </svg>
        WWW.TOMVARLEY.COM
      </li>
      <li class="contact-item"><span class="contact-mark"></span>@TOM_VARLEY_IMAGERY</li>
      <li class="contact-item"><span class="contact-mark"></span>@TOMVARLEYIMAGERY</li>
      <li class="contact-item"><span class="contact-mark round"></span>@TOM_VARLEY</li>
    </ul>

    <div class="brand">
      <span class="brand-dot"></span>
      <p class="brand-name">Tom Varley</p>
      <p class="brand-sub">Imagery</p>
    </div>
  </section>
</main>
</body>
</html>
```